Human Resources Flyer design

Create a 1 page flyer design for a staffing company that is looking to provide its services to clients. Images centered around people and businesses.
Target Market(s)
Large businesses
Industry/Entity Type
Staffing
Requirements
Must have
- Use color scheme that matches morvanhire.example.
Nice to have
- Flow chart like image for 3 areas mentioned.
- Images that convey professionalism and people connections

```html
<!DOCTYPE html>
<html lang="en">
<head>
<meta charset="utf-8">
<title>Morvan Hire – Staffing Flyer</title>
<link href="https://fonts.googleapis.com/css2?family=Arimo:wght@400;700&display=swap" rel="stylesheet">
<style>
  :root {
    --page: #e9e6e1;
    --flyer-top: #2b3442;
    --flyer-bottom: #1b222c;
    --ink: #ffffff;
    --ink-soft: #d9dee6;
    --accent: #f4a81d;
    --brand-red: #d4283a;
    --brand-grey: #c9ccd2;
  }
  * { box-sizing: border-box; margin: 0; padding: 0; }
  html, body {
    width: 1200px; height: 1200px; overflow: hidden;
    background: var(--page);
    font-family: "Arimo", Arial, sans-serif;
  }
  .flyer {
    position: absolute; left: 210px; top: 35px;
    width: 780px; height: 1130px;
    background:
      linear-gradient(100deg, rgba(255,255,255,0.04) 0 30%, transparent 30% 60%, rgba(255,255,255,0.03) 60%),
      linear-gradient(180deg, var(--flyer-top), var(--flyer-bottom));
    color: var(--ink);
    box-shadow: 0 6px 24px rgba(0,0,0,0.25);
  }
  .brand {
    position: absolute; left: 42px; top: 68px;
    display: flex; align-items: center; gap: 14px;
  }
  .brand-dot { width: 40px; height: 40px; border-radius: 50%; background: var(--brand-red); }
  .brand-name {
    font-size: 50px; font-weight: 700; color: var(--brand-red);
    letter-spacing: 1px; line-height: 1;
  }
  .intro {
    position: absolute; left: 40px; top: 205px; width: 690px;
    font-size: 13.5px; line-height: 1.45; color: var(--ink-soft);
  }
  .expect { position: absolute; left: 167px; top: 288px; font-size: 13.5px; line-height: 1.4; }
  .section-title {
    display: block; font-size: 15px; font-weight: 700; color: var(--accent);
    text-decoration: underline; text-underline-offset: 2px;
  }
  .stage { position: absolute; font-size: 13.5px; line-height: 1.45; }
  .stage p { color: var(--ink); }
  .stage ul { list-style: none; margin-top: 12px; }
  .stage li { padding-left: 12px; position: relative; color: var(--ink-soft); }
  .stage li::before { content: "•"; position: absolute; left: 0; }
  .stage-tactical { left: 401px; top: 352px; width: 350px; }
  .stage-supervisor { left: 44px; top: 582px; width: 345px; }
  .stage-business { left: 399px; top: 846px; width: 350px; }
  .photo {
    position: absolute; border-radius: 70px;
    box-shadow: 0 0 0 3px rgba(255,255,255,0.08);
  }
  .photo-workshop {
    left: 90px; top: 345px; width: 298px; height: 165px;
    background: linear-gradient(120deg, #5b6878, #3a4656 45%, #8a7b68 80%, #4b5563);
  }
  .photo-meeting {
    left: 403px; top: 585px; width: 273px; height: 163px;
    background: linear-gradient(135deg, #cfd8e3, #7a8898 45%, #2e3846);
  }
  .photo-teamwork {
    left: 90px; top: 897px; width: 278px; height: 150px;
    background: linear-gradient(160deg, #6d7886, #9a8a74 50%, #3c4654);
  }
  .step {
    position: absolute; width: 44px; height: 44px; border-radius: 50%;
    background: var(--brand-red); color: #fff; border: 3px solid #fff;
    font-size: 22px; font-weight: 700;
    display: flex; align-items: center; justify-content: center;
  }
  .step-1 { left: 49px; top: 400px; }
  .step-2 { left: 681px; top: 646px; }
  .step-3 { left: 39px; top: 947px; }
</style>
</head>
<body>
  <main class="flyer">
    <header class="brand">
      <span class="brand-dot"></span>
      <span class="brand-name">MORVAN HIRE</span>
    </header>

    <p class="intro">Morvan Hire combines the best tools in human resource and risk management with industry-leading knowledge to create a unique operational platform. “Our expertise in human resource management, risk mitigation and safety, payroll administration, workers’ compensation coverage and employee benefits allow our clients to focus on their core business”</p>

    <div class="expect">
      <span class="section-title">What you can expect from Morvan</span>
      Business owners working with Morvan typically move through three stages.
    </div>

    <div class="photo photo-workshop" role="img" aria-label="Worker wearing safety glasses assembling equipment in a workshop"></div>
    <span class="step step-1">1</span>
    <section class="stage stage-tactical">
      <span class="section-title">Tactical Alignment</span>
      <p>The first stage addresses the administrative and tactical components of managing your employees.</p>
      <ul>
        <li>Analysis of safety programs and HR practices</li>
        <li>Establish payroll submission and administration protocol</li>
        <li>Hiring, selection and new hire onboarding best practices</li>
        <li>Injury reporting protocol</li>
        <li>Establishing goals and creation of action plan</li>
        <li>Identification of metrics to track effectiveness</li>
      </ul>
    </section>

    <section class="stage stage-supervisor">
      <span class="section-title">Supervisor Development</span>
      <p>The second stage of the relationship focuses on continuing process improvement, further development of HR, risk and payroll best practices, as well as supervisor development. Examples include :</p>
      <ul>
        <li>Ongoing development and refinement of action plans</li>
        <li>Supervisory skill development and training (workplace safety, effective human capital management, and overall risk mitigation)</li>
        <li>Platform of performance management and performance improvement</li>
        <li>Evaluation of employee benefits options</li>
      </ul>
    </section>
    <div class="photo photo-meeting" role="img" aria-label="Business team seated at a conference table during a meeting"></div>
    <span class="step step-2">2</span>

    <div class="photo photo-teamwork" role="img" aria-label="Overhead view of colleagues collaborating around a desk with laptops and papers"></div>
    <span class="step step-3">3</span>
    <section class="stage stage-business">
      <span class="section-title">Business-level Guidance</span>
      <p>Activities involved in the third stage of the relationship are more strategic and forward-looking with a goal of cultivating an environment in your organization in which employees and supervisors drive the success of the organization instead of you, the business owner. Areas of focus may include:</p>
      <ul>
        <li>Strategic planning</li>
        <li>Proactive mitigation of business risks</li>
        <li>Holistic view of where your business is going</li>
        <li>Leadership development and succession planning</li>
        <li>Organizational development and design</li>
      </ul>
    </section>
  </main>
</body>
</html>
```